Talbrin Business Cards

Front and back. Simon Kavelle MBA is the CEO of Talbrin Homes. Black white and grays. Logo and cool design.

Target Market(s)

Professional lenders and investors

Industry/Entity Type

Real estate developer. NO HOUSES OR ROOFS

Contact Information for Business Card

Logo, name and unique design. Front and back. Simon Kavelle MBA is the CEO of Talbrin Homes. Black white and grays. Logo and cool design.

Font styles to use
Sans Serif

Colors

Designer to choose only greyscale colors for use in the design.

Requirements
Must have
• Cool look. Not the same card I could design.
Nice to have
• Something memorable
Should not have
• Basic

```html
<!DOCTYPE html>
<html lang="en">
<head>
<meta charset="utf-8">
<title>Talbrin Homes – Business Cards</title>
<link href="https://fonts.googleapis.com/css2?family=Montserrat:wght@300;400;600;800&display=swap" rel="stylesheet">
<style>
  :root {
    --page-bg: #2a2a2c;
    --card-black: #0e0e0f;
    --card-gloss: #1f1f21;
    --ink-white: #f4f4f4;
    --ink-grey: #8a8a8a;
    --ink-dim: #6a6a6c;
    --rule-grey: #3a3a3c;
    --accent-grey: #4a4a4c;
  }
  * { margin: 0; padding: 0; box-sizing: border-box; }
  html, body {
    width: 1200px; height: 800px; overflow: hidden;
    background: var(--page-bg);
    font-family: "Montserrat", sans-serif;
  }
  .canvas {
    width: 1200px; height: 800px;
    display: flex; align-items: center; justify-content: center; gap: 40px;
  }
  .card {
    position: relative;
    width: 540px; height: 309px;
    border-radius: 22px;
    background: var(--card-black);
    overflow: hidden;
    box-shadow: 0 18px 40px rgba(0,0,0,.45);
  }

  /* Front */
  .card--front { display: flex; align-items: center; justify-content: center; }
  .front-wordmark {
    font-weight: 800; font-size: 52px; letter-spacing: -1px;
    color: var(--card-gloss);
    white-space: nowrap;
  }

  /* Back */
  .back-brand-band {
    position: absolute; top: 0; right: 0; bottom: 0; width: 132px;
    border-left: 1px solid var(--rule-grey);
    display: flex; align-items: center; justify-content: center;
  }
  .back-wordmark {
    transform: rotate(90deg);
    font-weight: 800; font-size: 32px; letter-spacing: -0.5px;
    color: var(--ink-white);
    white-space: nowrap;
  }
  .edge-mark { position: absolute; background: var(--ink-dim); }
  .edge-mark--top { top: 50px; right: 131px; width: 2px; height: 40px; }
  .edge-mark--bottom { bottom: 50px; right: 131px; width: 2px; height: 40px; }
  .edge-mark--tab { left: 0; top: 108px; width: 14px; height: 34px; background: var(--accent-grey); }
  .edge-mark--foot { left: 44px; bottom: 0; width: 1px; height: 22px; background: var(--rule-grey); }

  .identity { position: absolute; left: 44px; top: 102px; }
  .identity__name {
    font-weight: 300; font-size: 21px; color: var(--ink-white);
    letter-spacing: .5px; text-transform: uppercase;
  }
  .identity__name strong { font-weight: 600; }
  .identity__role {
    margin-top: 3px;
    font-weight: 300; font-size: 12.5px; color: var(--ink-dim);
    letter-spacing: .8px; text-transform: uppercase;
  }

  .contact-list { position: absolute; left: 44px; bottom: 36px; list-style: none; }
  .contact-list li {
    display: flex; align-items: center; gap: 10px;
    font-weight: 400; font-size: 14px; color: var(--ink-white);
    letter-spacing: .4px; line-height: 24px;
  }
  .contact-list svg { width: 13px; height: 13px; fill: var(--ink-grey); flex: none; }
</style>
</head>
<body>
<main class="canvas">

  <section class="card card--front" aria-label="Card front">
    <div class="front-wordmark">Talbrin Homes</div>
  </section>

  <section class="card card--back" aria-label="Card back">
    <span class="edge-mark edge-mark--tab"></span>
    <span class="edge-mark edge-mark--top"></span>
    <span class="edge-mark edge-mark--bottom"></span>
    <span class="edge-mark edge-mark--foot"></span>

    <div class="identity">
      <p class="identity__name">Simon <strong>Kavelle</strong> MBA</p>
      <p class="identity__role">CEO of Talbrin Homes</p>
    </div>

    <ul class="contact-list">
      <li>
        <svg viewBox="0 0 24 24" aria-hidden="true"><path d="M6.6 10.8a15 15 0 0 0 6.6 6.6l2.2-2.2a1 1 0 0 1 1-.25 11.4 11.4 0 0 0 3.6.57 1 1 0 0 1 1 1V20a1 1 0 0 1-1 1A17 17 0 0 1 3 4a1 1 0 0 1 1-1h3.5a1 1 0 0 1 1 1c0 1.25.2 2.45.57 3.57a1 1 0 0 1-.25 1z"/></svg>
        555-018-7314
      </li>
      <li>
        <svg viewBox="0 0 24 24" aria-hidden="true"><path d="M2 5h20v14H2z M2 5l10 8 10-8" /></svg>
        Simon@talbrinhomes.com
      </li>
      <li>
        <svg viewBox="0 0 24 24" aria-hidden="true"><path d="M12 2a10 10 0 1 0 0 20 10 10 0 0 0 0-20zm0 2c.9 1.2 1.6 2.6 2 4h-4c.4-1.4 1.1-2.8 2-4zM4.3 14a8 8 0 0 1 0-4h3.4a17 17 0 0 0 0 4zm.9 2h3a13 13 0 0 0 1.4 3.5A8 8 0 0 1 5.2 16zm3-8h-3a8 8 0 0 1 4.4-3.5A13 13 0 0 0 8.2 8zM12 20c-.9-1.2-1.6-2.6-2-4h4c-.4 1.4-1.1 2.8-2 4zm2.3-6H9.7a15 15 0 0 1 0-4h4.6a15 15 0 0 1 0 4zm.1 5.5A13 13 0 0 0 15.8 16h3a8 8 0 0 1-4.4 3.5zM16.3 14a17 17 0 0 0 0-4h3.4a8 8 0 0 1 0 4zm-.5-6a13 13 0 0 0-1.4-3.5A8 8 0 0 1 18.8 8z"/></svg>
        www.talbrinhomes.com
      </li>
    </ul>

    <div class="back-brand-band">
      <div class="back-wordmark">Talbrin Homes</div>
    </div>
  </section>

</main>
</body>
</html>
```